Book Cover Design - Rooted Together: 7 Paths to Raise a Home that Flourishes

International cover needed for the Australian (Marlow Fenwick/QRT Press 2011) non-fiction book Rooted Together: 7 Paths to Raise a Home that Flourishes.

Blurb: With the birth of a baby, come other new beginnings, the birth of a mother, of a father, and of a family. With each stage of a child's growth, and with every new baby, there are more new beginnings. In older cultures and in villages around the world, parenthood was considered a rite of passage but traditions that guided parents into becoming a family have largely been lost - until now.

This ground breaking book walks a new generation of mothers and fathers through the eight steps of the modern parenthood rite of passage, from couple-connection to family-foundations, so they can prepare for and continue to grow a family that thrives.

Bio: Mara Quinlan is a relationship counsellor, parent educator and columnist for Sensible Homelife magazine. She lives in Sydney with her husband, their three gorgeous children and an itinerary of pets. This is her first book.
Updates

Thank you for your patience, I haven't ever done anything like this before and the designs submitted have helped me to be more specific in my requests. Please see the updated brief. The most important point is that I am seeking a TEXT based cover, so BOTH the TITLE and SUBTITLE should take up most of the space, the image could either be in the background with the title and subtitle overlayed, or be much smaller to fit around them. I have attached some more images to the brief, hope they help to convey the 'feel' I am after.  Thanks again!

Reason: Thank you so much for taking an interest in this project, the process has been very educational and helpful for me. While some of the stock art in the submitted designs are great, I've decided to commission a custom illustration which completely captures the meaning of Rooted Together. I will upload the illustration once it's complete for designers who are still interested to use. Thank you for your patience! Mara

Thank you all for your patience and for opening up my thinking about what I am really hoping for with this cover. I have uploaded some new tree designs and more specific instructions that I would like to be included in the cover design. I'm looking forward to seeing your creations!

With warm regards,

Mara

Target Market(s)

Couples thinking about having a baby and new parents of one or more young children.

Industry/Entity Type

Baby

Requirements
Must have
• TEXT based cover with BOTH the TITLE and SUBTITLE taking up most of the page.
Colors to match the Australian version (see attached)
Tree design bottom left (as per Trunk Treatment image attached) OR Heart Tree Design
Root design (as per one of the two images attached)
PLEASE ADD: three new shoots coming up from the ground under the tree to symbolize the children.
Nice to have
• Artistic effect to complement Australian cover.
Subtle retro feel to complement Australian cover.
Should not have
• The book is inclusive of all parents (including same-sex parents) so no images of mother/father and baby.

```html
<!DOCTYPE html>
<html lang="en">
<head>
<meta charset="utf-8">
<title>Rooted Together — Book Cover</title>
<link rel="stylesheet" href="https://fonts.googleapis.com/css2?family=Federo&family=Federant&display=swap">
<style>
  :root {
    --ink-navy: #363a94;
    --ink-green: #1f7a3c;
    --ink-white: #ffffff;
    --sky-pale: #f2f6fa;
    --sky-mid: #d3e8f5;
    --sky-deep: #8fcdf0;
    --meadow-light: #cbdd4c;
    --meadow-mid: #a8c73a;
    --meadow-deep: #7fa42a;
  }
  html, body {
    margin: 0;
    padding: 0;
    width: 802px;
    height: 1200px;
    overflow: hidden;
    background: var(--sky-pale);
  }
  .cover {
    position: relative;
    width: 802px;
    height: 1200px;
    overflow: hidden;
  }
  .sky {
    position: absolute;
    inset: 0;
    background: linear-gradient(180deg,
      var(--sky-pale) 0%,
      var(--sky-mid) 40%,
      var(--sky-deep) 70%,
      var(--sky-mid) 85%);
  }
  .meadow-art {
    position: absolute;
    left: 0;
    top: 720px;
    width: 802px;
    height: 480px;
  }
  .title-rule {
    position: absolute;
    left: 166px;
    width: 468px;
    height: 2px;
    background: var(--ink-navy);
  }
  .title-rule--top { top: 160px; }
  .title-rule--bottom { top: 610px; }
  .title-lead {
    position: absolute;
    top: 162px;
    left: 0;
    width: 802px;
    margin: 0;
    text-align: center;
    font-family: "Federo", sans-serif;
    font-weight: 400;
    font-size: 96px;
    line-height: 1;
    color: var(--ink-navy);
    letter-spacing: 1px;
  }
  .title-main {
    position: absolute;
    top: 274px;
    left: 166px;
    width: 468px;
    height: 326px;
    overflow: visible;
  }
  .title-main text {
    font-family: "Federo", sans-serif;
    fill: var(--ink-navy);
  }
  .subtitle {
    position: absolute;
    top: 620px;
    left: 0;
    width: 802px;
    margin: 0;
    text-align: center;
    font-family: "Federant", serif;
    font-size: 38px;
    line-height: 48px;
    color: var(--ink-green);
  }
  .author {
    position: absolute;
    top: 1078px;
    left: 0;
    width: 802px;
    margin: 0;
    text-align: center;
    font-family: "Federant", serif;
    font-size: 50px;
    line-height: 1;
    color: var(--ink-white);
    letter-spacing: 2px;
  }
</style>
</head>
<body>
  <main class="cover">
    <div class="sky" role="img" aria-label="Watercolour sky with soft white clouds"></div>

    <svg class="meadow-art" viewBox="0 0 802 480" role="img" aria-label="Watercolour green hill with a tree at bottom left showing its roots, three small shoots under it, and a second tree on the right">
      <defs>
        <radialGradient id="meadow-tone" cx="0.2" cy="0.25" r="1">
          <stop offset="0" stop-color="var(--meadow-light)"/>
          <stop offset="0.55" stop-color="var(--meadow-mid)"/>
          <stop offset="1" stop-color="var(--meadow-deep)"/>
        </radialGradient>
        <linearGradient id="canopy-tone" x1="0" y1="0" x2="0" y2="1">
          <stop offset="0" stop-color="var(--meadow-light)" stop-opacity="0.85"/>
          <stop offset="1" stop-color="var(--meadow-mid)" stop-opacity="0"/>
        </linearGradient>
      </defs>
      <rect x="0" y="0" width="300" height="330" rx="150" fill="url(#canopy-tone)"/>
      <rect x="590" y="30" width="200" height="300" rx="100" fill="url(#canopy-tone)"/>
      <path d="M0 320 Q 400 240 802 300 L 802 480 L 0 480 Z" fill="url(#meadow-tone)"/>
    </svg>

    <div class="title-rule title-rule--top"></div>
    <h1 class="title-lead">Rooted</h1>
    <svg class="title-main" viewBox="0 0 468 326" aria-label="Together">
      <text x="0" y="110" font-size="150" textLength="468" lengthAdjust="spacingAndGlyphs" transform="scale(1,2.96)">TOGETHER</text>
    </svg>
    <div class="title-rule title-rule--bottom"></div>

    <p class="subtitle">7 Paths to Raise a<br>Home that Flourishes</p>

    <p class="author">Mara Quinlan</p>
  </main>
</body>
</html>
```